Cat sitting business Web Design Project ***

I have a cat sitting business where I either take care of cats in their home or board them in mine

I need a website which offers my services, my rates, about me, FAQ's, Hours of operation and service areas covered, testimonials, contact info, newsletter sign up, gallery of photos and the ability for me to go in and update when needed.

Coded - Design and coding required

5+ page

```html
<!DOCTYPE html>
<html lang="en">
<head>
<meta charset="utf-8">
<title>Cozy Whisker Cat Sitting</title>
<link href="https://fonts.googleapis.com/css2?family=Poppins:wght@400;500;600;700&display=swap" rel="stylesheet">
<style>
:root{
  --ink:#0d3b45;
  --deep:#0b3a44;
  --green:#6db04a;
  --green-dark:#1f6b4f;
  --teal-light:#d3f0ec;
  --teal-mid:#a8dcd6;
  --mint:#e5f6f4;
  --cta:#d6f2dc;
  --text:#4b5d63;
  --white:#ffffff;
  --sand:#f4e3c8;
}
*{box-sizing:border-box;margin:0;padding:0}
html,body{width:1200px;height:3260px;overflow:hidden}
body{font-family:"Poppins",sans-serif;color:var(--ink);background:var(--white);position:relative}
.abs{position:absolute}
.topbar{top:0;left:0;width:1200px;height:36px;background:var(--deep);color:var(--white);font-size:13px;font-weight:500;text-align:center;line-height:36px}
.nav{top:36px;left:0;width:1200px;height:90px;background:var(--white)}
.brand{position:absolute;left:100px;top:24px;display:flex;align-items:center;gap:10px;font-size:16px;font-weight:600;color:var(--green-dark);line-height:1.15}
.brand-dot{width:38px;height:38px;border-radius:50%;background:var(--mint)}
.nav-links{position:absolute;left:325px;top:34px;display:flex;gap:26px;font-size:15px;font-weight:500}
.signup{position:absolute;left:880px;top:34px;font-size:15px;font-weight:500}
.btn{display:inline-block;border-radius:8px;font-weight:600;font-size:15px;text-align:center}
.btn-green{background:var(--green);color:var(--white)}
.btn-white{background:var(--white);color:var(--ink)}
.btn-outline{border:2px solid var(--green);color:var(--green-dark)}
.login{position:absolute;left:965px;top:20px;width:135px;height:56px;line-height:56px}
.hero{top:126px;left:0;width:1200px;height:610px;background:linear-gradient(180deg,var(--teal-light),var(--teal-mid));overflow:hidden}
.hero h1{position:absolute;left:100px;top:100px;width:520px;font-size:38px;line-height:1.2;font-weight:700}
.hero p{position:absolute;left:100px;top:254px;width:470px;font-size:16px;line-height:1.55;color:var(--ink)}
.hero .btn{position:absolute;left:100px;top:352px;width:122px;height:56px;line-height:56px}
.hero-photo{position:absolute;left:660px;top:0;width:540px;height:610px;background:linear-gradient(90deg,rgba(168,220,214,0) 0%,#cfb493 22%,#c39a70 55%,#b58a62 80%,rgba(168,220,214,0.6) 100%)}
.hero-wave{top:660px;left:0}
.about-photo-back{left:118px;top:818px;width:372px;height:386px;background:var(--sand);transform:rotate(3deg)}
.about-photo{left:100px;top:800px;width:372px;height:386px;background:linear-gradient(160deg,#8a7d76,#3f3a3a 55%,#d9d4d2);border-radius:6px}
.about h2{position:absolute;left:545px;top:808px;width:520px;font-size:30px;line-height:1.25;color:var(--green-dark);font-weight:700}
.about p{position:absolute;left:545px;top:922px;width:500px;font-size:15px;line-height:1.55;color:var(--text)}
.about .btn{position:absolute;left:545px;top:1064px;width:172px;height:60px;line-height:60px}
.features{top:1240px;left:0;width:1200px;height:510px;background:var(--mint)}
.features h2{position:absolute;left:0;top:90px;width:1200px;text-align:center;font-size:32px;line-height:1.3;font-weight:700}
.feat{position:absolute;display:flex;align-items:center;gap:22px;font-size:16px;font-weight:500;line-height:1.35;width:300px}
.feat-icon{width:74px;height:74px;border-radius:50%;border:2px solid var(--ink);background:var(--white);display:flex;align-items:center;justify-content:center;flex-shrink:0}
.gallery h2{position:absolute;left:100px;top:1808px;width:720px;font-size:32px;line-height:1.25;font-weight:700;color:var(--green-dark)}
.gallery .btn{position:absolute;left:890px;top:1822px;width:210px;height:62px;line-height:62px;font-size:17px}
.shot{position:absolute;border-radius:8px}
.cta{top:2500px;left:0;width:1200px;height:390px;background:var(--cta);overflow:hidden}
.cta h2{position:absolute;left:130px;top:56px;width:520px;font-size:28px;line-height:1.3;font-weight:700}
.cta .b1{position:absolute;left:130px;top:200px;width:180px;height:58px;line-height:58px}
.cta .b2{position:absolute;left:332px;top:200px;width:160px;height:58px;line-height:54px}
.kittens{position:absolute;left:680px;top:140px;width:520px;height:250px;background:linear-gradient(90deg,rgba(214,242,220,0) 0%,#c79563 18%,#d69c5e 60%,#dfa862 85%,rgba(214,242,220,0.4) 100%)}
.bubble{position:absolute;background:var(--white);border-radius:8px;font-size:16px;font-weight:500;padding:10px 20px;box-shadow:0 2px 6px rgba(0,0,0,.08)}
.footer{top:2890px;left:0;width:1200px;height:370px;background:var(--deep);color:var(--white)}
.footer-brand{position:absolute;left:490px;top:30px;width:220px;height:82px;background:var(--white);border-radius:8px;display:flex;align-items:center;justify-content:center;gap:10px;font-size:16px;font-weight:600;color:var(--green-dark);line-height:1.15}
.footer-links{position:absolute;left:0;top:162px;width:1200px;display:flex;justify-content:center;gap:30px;font-size:15px;font-weight:500}
.footer p{position:absolute;left:420px;top:198px;width:360px;text-align:center;font-size:13px;line-height:1.5}
.socials{position:absolute;left:0;top:300px;width:1200px;display:flex;justify-content:center;gap:18px}
.socials span{width:20px;height:20px;border-radius:50%;background:var(--white)}
</style>
</head>
<body>

<div class="abs topbar">Lorem ipsum dolor sit amet, consectetur adipiscing elit.</div>

<header class="abs nav">
  <div class="brand"><span class="brand-dot"></span><span>Cozy Whisker<br>Cat Sitting</span></div>
  <nav class="nav-links"><span>Services</span><span>About</span><span>Contact</span><span>Gallery</span></nav>
  <span class="signup">Sign up</span>
  <span class="btn btn-green login">Log in</span>
</header>

<section class="abs hero">
  <div class="hero-photo" role="img" aria-label="Photo of a tabby cat reaching up with one paw"></div>
  <h1>We'll take care of your cats, because they deserve the best!</h1>
  <p>Cat baby sitting starts at home, and with our business, you can access reliable cat sitting services, with affordable costs</p>
  <span class="btn btn-white">Get Started</span>
</section>
<svg class="abs hero-wave" width="1200" height="90" viewBox="0 0 1200 90">
  <path d="M0 30 C250 80 450 10 650 40 S1000 70 1200 20 V90 H0Z" fill="#fff"/>
  <path d="M0 30 C250 80 450 10 650 40 S1000 70 1200 20" fill="none" stroke="#6db04a" stroke-width="6"/>
</svg>

<section class="about">
  <div class="abs about-photo-back"></div>
  <div class="abs about-photo" role="img" aria-label="Photo of the cat sitter holding a white cat"></div>
  <h2>Get your cats a new friendly home with our services 🐾</h2>
  <p>Hey, this is X. Being a cat lover and a pet owner myself, I can relate to the struggle of finding someone trustworthy to care for your pets when you are not around. You can book my service and rest assured I will take care of them when you need to be somewhere else</p>
  <span class="btn btn-green">Our Services</span>
</section>

<section class="abs features">
  <svg class="abs" style="left:0;top:-40px" width="1200" height="60" viewBox="0 0 1200 60"><path d="M0 60 C300 0 700 60 1200 10 V60Z" fill="#e5f6f4"/></svg>
  <h2>Lorem ipsum dolor sit amet,<br>consectetur adipiscing elit.</h2>
  <div class="feat" style="left:268px;top:206px">
    <span class="feat-icon"><svg width="36" height="36" viewBox="0 0 36 36" fill="none" stroke="#0d3b45" stroke-width="2"><path d="M6 28c2-8 8-12 14-12s8 4 8 8-4 6-8 6H8"/><path d="M24 16l2-6 3 4"/></svg></span>
    <span>Your cats' best<br>play-zone</span>
  </div>
  <div class="feat" style="left:620px;top:206px">
    <span class="feat-icon"><svg width="36" height="36" viewBox="0 0 36 36" fill="none" stroke="#0d3b45" stroke-width="2"><path d="M18 4v8M18 24v8M4 18h8M24 18h8M9 9l5 5M22 22l5 5M27 9l-5 5M14 22l-5 5"/></svg></span>
    <span>Clean &amp; Healthy<br>Surroundings</span>
  </div>
  <div class="feat" style="left:268px;top:354px">
    <span class="feat-icon"><svg width="36" height="36" viewBox="0 0 36 36" fill="none" stroke="#0d3b45" stroke-width="2"><rect x="5" y="10" width="26" height="20" rx="3"/><path d="M5 12l13 9 13-9"/></svg></span>
    <span>Most comfortable<br>environment</span>
  </div>
  <div class="feat" style="left:620px;top:354px">
    <span class="feat-icon"><svg width="36" height="36" viewBox="0 0 36 36" fill="none" stroke="#0d3b45" stroke-width="2"><rect x="8" y="8" width="20" height="22" rx="3"/><path d="M8 14h20"/><circle cx="18" cy="22" r="4"/></svg></span>
    <span>Finest Cat Foods</span>
  </div>
</section>

<section class="gallery">
  <h2>It's a big cat family! Check out some photos of our lovely members</h2>
  <span class="btn btn-green">View All →</span>
  <div class="shot" style="left:100px;top:1930px;width:232px;height:250px;background:linear-gradient(150deg,#8a3a3a,#e6ddd5)" role="img" aria-label="Photo of a white and grey cat lying on a red blanket"></div>
  <div class="shot" style="left:100px;top:2196px;width:232px;height:270px;background:linear-gradient(150deg,#c58a55,#7b6a5c)" role="img" aria-label="Photo of an orange and white cat being held"></div>
  <div class="shot" style="left:354px;top:1930px;width:232px;height:224px;background:linear-gradient(150deg,#d8cfc2,#9d8c7a)" role="img" aria-label="Photo of a tabby cat sitting on a floor"></div>
  <div class="shot" style="left:354px;top:2172px;width:232px;height:294px;background:linear-gradient(150deg,#9b8a74,#5e5348)" role="img" aria-label="Photo of a tabby cat looking up"></div>
  <div class="shot" style="left:610px;top:1930px;width:232px;height:360px;background:linear-gradient(150deg,#b9b3ad,#7c766f)" role="img" aria-label="Photo of a grey and white cat wearing a red bow"></div>
  <div class="shot" style="left:610px;top:2306px;width:232px;height:160px;background:linear-gradient(150deg,#e0c9c4,#a78f88)" role="img" aria-label="Photo of a cat on a pink floor"></div>
  <div class="shot" style="left:866px;top:1930px;width:234px;height:234px;background:linear-gradient(150deg,#c9c6c2,#3a3634)" role="img" aria-label="Photo of a dark cat by a window"></div>
  <div class="shot" style="left:866px;top:2196px;width:234px;height:270px;background:linear-gradient(150deg,#6a5a4a,#d8d2cc)" role="img" aria-label="Photo of a black and white cat sitting on a shelf"></div>
</section>

<section class="abs cta">
  <h2>Lorem ipsum dolor sit amet, Learn more about us. If you have any query, let us know</h2>
  <span class="btn btn-green b1">Contact us</span>
  <span class="btn btn-outline b2">Read FAQs</span>
  <div class="kittens" role="img" aria-label="Photo of two kittens peeking up"></div>
  <span class="bubble" style="left:722px;top:82px">Meow 🥰</span>
  <span class="bubble" style="left:1010px;top:130px">Hi User</span>
</section>

<footer class="abs footer">
  <div class="footer-brand"><span class="brand-dot"></span><span>Cozy Whisker<br>Cat Sitting</span></div>
  <nav class="footer-links"><span>Home</span><span>Service</span><span>About</span><span>Contact</span><span>Gallery</span></nav>
  <p>Lorem ipsum dolor sit amet, cozy visits at home or boarding with us. Gentle daily care, fresh food and play. Friendly sitters who love cats. Book a stay today and relax.</p>
  <div class="socials"><span></span><span></span><span></span><span></span></div>
</footer>

</body>
</html>
```